QVM Business Card Design

We need a refreshed business card. Our company is a venture capital investment firm focused on investing in medical devices. Logo is attached. please also see our website www.qvmholdings.example

Target Market(s)

investors and potential investment targets

Industry/Entity Type

medical investments

Contact Information for Business Card

logo, name, title, email, phone, website, address,

Colors
0054AA
0677BA
7BADD7
CADEEF
E8F1F8
0094D4
00A9DD
6FCCEA
C7EBF8
E9F6FB
00AB8E
00BBA5
67D7C9
C6EFE9
E9F9F6

Requirements
Must have
• fresh modern design
Nice to have
• QR code leading to our linked in page, short description of what we do “Early Stage Medical Device Investors”

```html
<!DOCTYPE html>
<html lang="en">
<head>
<meta charset="utf-8">
<title>QVM Business Card</title>
<link rel="stylesheet" href="https://fonts.googleapis.com/css2?family=Montserrat:wght@400;500;700;800&display=swap">
<style>
  :root {
    --brand-blue: #0054AA;
    --back-blue: #0B5BB2;
    --back-blue-deep: #084C97;
    --teal: #00AB8E;
    --teal-pale: #C6EFE9;
    --teal-mist: #E9F9F6;
    --link-blue: #0677BA;
    --ink: #2B2B2B;
    --paper: #FFFFFF;
    --stage: #E6E8EB;
  }
  * { margin: 0; padding: 0; box-sizing: border-box; }
  html, body { width: 1200px; height: 900px; overflow: hidden; }
  body {
    background: var(--stage);
    font-family: "Montserrat", Arial, sans-serif;
    position: relative;
  }
  .card {
    position: absolute;
    left: 260px;
    width: 680px;
    height: 388px;
    border-radius: 22px;
    overflow: hidden;
    box-shadow: 0 6px 18px rgba(0,0,0,0.12);
  }
  .card--front { top: 42px; background: var(--paper); }
  .card--back { top: 470px; background: var(--back-blue); }

  .front__decor {
    position: absolute;
    left: 250px; top: 70px;
    width: 190px; height: 290px;
    border-radius: 40px;
    background: radial-gradient(ellipse at center, var(--teal-pale) 0%, var(--teal-mist) 55%, rgba(255,255,255,0) 75%);
    opacity: 0.7;
  }
  .brand { position: absolute; left: 220px; top: 30px; text-align: center; }
  .brand__name {
    font-weight: 800; font-size: 72px; line-height: 1;
    color: var(--brand-blue); letter-spacing: 2px;
  }
  .brand__tagline {
    margin-top: 8px;
    font-size: 12.5px; font-weight: 500; color: var(--ink);
    letter-spacing: 0.5px; white-space: nowrap;
  }
  .divider {
    position: absolute; left: 0; top: 164px;
    width: 560px; height: 2px; background: var(--teal);
  }
  .person { position: absolute; right: 34px; top: 126px; text-align: right; }
  .person__name {
    font-weight: 800; font-size: 29px; color: var(--brand-blue);
    letter-spacing: 1px; line-height: 36px;
  }
  .person__title { font-size: 17px; color: var(--ink); margin-top: 4px; }

  .contacts { position: absolute; left: 26px; top: 224px; list-style: none; }
  .contacts li {
    display: flex; align-items: center; gap: 8px;
    font-size: 18px; color: var(--ink); line-height: 30px;
  }
  .contacts svg { width: 15px; height: 15px; flex: none; }
  .contacts .web-domain { color: var(--link-blue); }

  .address {
    position: absolute; right: 30px; bottom: 34px;
    display: flex; align-items: center; gap: 10px;
  }
  .address__lines { text-align: right; font-size: 18px; color: var(--ink); line-height: 27px; }
  .address svg { width: 16px; height: 22px; }

  .back__texture {
    position: absolute; inset: 0;
    background: linear-gradient(135deg, var(--back-blue) 0%, var(--back-blue-deep) 100%);
  }
  .back__mark {
    position: absolute; left: 44px; bottom: 36px;
    font-weight: 800; font-size: 56px; color: var(--paper); letter-spacing: 2px;
  }
</style>
</head>
<body>

<section class="card card--front">
  <div class="front__decor" role="img" aria-label="Faint teal pulse-line decoration"></div>

  <div class="brand">
    <div class="brand__name">QVM</div>
    <div class="brand__tagline">QUALITY VENTURE MEDICINE</div>
  </div>

  <div class="divider"></div>

  <div class="person">
    <div class="person__name">JORDAN REYES</div>
    <div class="person__title">Director</div>
  </div>

  <ul class="contacts">
    <li>
      <svg viewBox="0 0 16 16" aria-hidden="true"><rect x="4" y="1" width="8" height="14" rx="1.5" fill="none" stroke="#0054AA" stroke-width="1.6"/><circle cx="8" cy="12.5" r="0.9" fill="#0054AA"/></svg>
      555-300-0147
    </li>
    <li>
      <svg viewBox="0 0 16 16" aria-hidden="true"><rect x="1" y="3" width="14" height="10" rx="1" fill="#0054AA"/><path d="M1.5 3.5 L8 9 L14.5 3.5" fill="none" stroke="#fff" stroke-width="1.2"/></svg>
      info@qvmholdings.example
    </li>
    <li>
      <svg viewBox="0 0 16 16" aria-hidden="true"><circle cx="8" cy="8" r="7" fill="#0054AA"/><path d="M1 8 H15 M8 1 C4 5 4 11 8 15 M8 1 C12 5 12 11 8 15" fill="none" stroke="#fff" stroke-width="1"/></svg>
      <span>www.<span class="web-domain">qvmholdings</span>.example</span>
    </li>
  </ul>

  <div class="address">
    <div class="address__lines">4820 W Linden, Fairview,<br>Ohio 44126</div>
    <svg viewBox="0 0 16 22" aria-hidden="true"><path d="M8 1 C3.5 1 1 4.2 1 7.6 C1 12 8 21 8 21 C8 21 15 12 15 7.6 C15 4.2 12.5 1 8 1 Z" fill="#0054AA"/><circle cx="8" cy="7.8" r="2.6" fill="#fff"/></svg>
  </div>
</section>

<section class="card card--back">
  <div class="back__texture" role="img" aria-label="Tone-on-tone embossed repeating pattern in deep blue"></div>
  <div class="back__mark">QVM</div>
</section>

</body>
</html>
```